VENTURE CAPITAL GROUP BUSINESS CARD DESIGN

Venture Capital Group based in SF looking for a bold business card design. No trendy colour explosion, 3D effects etc. Just "simple" optical effects. Works on your brain, keeps your eye focused and sticks to your mind.
Target Market(s)
Technology startups
Industry/Entity Type
Venture Capital
Contact Information for Business Card
BARNABY WHITLOCK
MANAGING PARTNER
817 FERN ST SAN FRANCISCO, CA 94111
415.555.0143 O
415.555.0167 F
415.555.0192 C
barn@halcyonridgefund.example

```html
<!DOCTYPE html>
<html lang="en">
<head>
<meta charset="utf-8">
<title>Halcyon Ridge Capital Group – Business Card</title>
<link rel="stylesheet" href="https://fonts.googleapis.com/css2?family=Merriweather:wght@400;700&family=Roboto+Condensed:wght@400&display=swap">
<style>
  :root {
    --backdrop: #a9a6a7;
    --card-dark: #1b1c1c;
    --card-light: #fbfbfb;
    --brand-green: #2e8b3c;
    --deep-green: #156a32;
    --bright-green: #4cb84f;
    --silver: #b9b9b9;
    --silver-dark: #8c8c8c;
    --ink-gray: #5a5a5a;
    --ink-light: #777777;
    --white: #ffffff;
  }
  * { margin: 0; padding: 0; box-sizing: border-box; }
  html, body { width: 1200px; height: 1200px; overflow: hidden; }
  body { background: var(--backdrop); position: relative; }

  .card { position: absolute; width: 714px; height: 420px; overflow: hidden; }
  .card-front { left: 243px; top: 116px; background: var(--card-dark); }
  .card-back  { left: 243px; top: 644px; background: var(--card-light); }

  .brand-disc { position: absolute; border-radius: 50%; }
  .card-front .brand-disc {
    width: 160px; height: 160px; left: 277px; top: 70px;
    background: radial-gradient(circle at 50% 40%, #2c2c2c, #141414);
    box-shadow: 0 0 6px rgba(255,255,255,0.12);
  }
  .card-back .brand-disc {
    width: 156px; height: 156px; left: 108px; top: 52px;
    background: radial-gradient(circle at 50% 40%, #ffffff, #e3e3e3);
  }

  .brand-name {
    position: absolute; text-align: center;
    font-family: 'Merriweather', serif; font-weight: 400;
    color: var(--brand-green); line-height: 1;
  }
  .card-front .brand-name { left: 0; width: 714px; top: 262px; font-size: 40px; letter-spacing: 1px; }
  .card-front .brand-tag  { left: 0; width: 714px; top: 312px; font-size: 13px; letter-spacing: 6px; }
  .card-back .brand-name  { left: 26px; width: 320px; top: 230px; font-size: 29px; letter-spacing: 1px; }
  .card-back .brand-tag   { left: 26px; width: 320px; top: 270px; font-size: 10px; letter-spacing: 5px; }

  .person { position: absolute; right: 38px; top: 54px; text-align: right; font-family: 'Merriweather', serif; }
  .person-name { font-size: 22px; font-weight: 700; color: var(--ink-gray); }
  .person-title { font-size: 15px; font-weight: 400; color: var(--ink-light); margin-top: 6px; }

  .wave { position: absolute; left: 0; top: 0; }

  .contact-list {
    position: absolute; right: 24px; top: 272px; list-style: none;
    font-family: 'Roboto Condensed', sans-serif; font-size: 17px; color: var(--white);
  }
  .contact-list li { display: flex; justify-content: flex-end; align-items: center; height: 24.5px; }
  .contact-list svg { width: 18px; height: 18px; margin-left: 12px; fill: var(--white); }
</style>
</head>
<body>

<section class="card card-front" aria-label="Card front">
  <div class="brand-disc"></div>
  <div class="brand-name">HALCYON RIDGE</div>
  <div class="brand-name brand-tag">CAPITAL GROUP</div>
</section>

<section class="card card-back" aria-label="Card back">
  <svg class="wave" width="714" height="420" viewBox="0 0 714 420" aria-hidden="true">
    <defs>
      <linearGradient id="greenBand" x1="0" y1="0" x2="1" y2="0">
        <stop offset="0" stop-color="var(--bright-green)"/>
        <stop offset="0.55" stop-color="var(--brand-green)"/>
        <stop offset="1" stop-color="var(--deep-green)"/>
      </linearGradient>
      <linearGradient id="silverBand" x1="0" y1="0" x2="1" y2="0">
        <stop offset="0" stop-color="#e2e2e2"/>
        <stop offset="0.5" stop-color="var(--silver)"/>
        <stop offset="1" stop-color="var(--silver-dark)"/>
      </linearGradient>
    </defs>
    <path d="M0,338 C140,352 270,350 390,300 C500,254 600,212 714,196 L714,210 C600,228 510,266 410,314 C290,372 150,380 0,366 Z" fill="url(#silverBand)"/>
    <path d="M40,344 C160,360 280,360 400,306 C300,368 160,372 40,344 Z" fill="var(--silver)" opacity="0.7"/>
    <path d="M0,372 C150,392 300,382 420,326 C520,278 610,232 714,224 L714,420 L0,420 Z" fill="url(#greenBand)"/>
  </svg>

  <div class="brand-disc"></div>
  <div class="brand-name">HALCYON RIDGE</div>
  <div class="brand-name brand-tag">CAPITAL GROUP</div>

  <div class="person">
    <div class="person-name">Barnaby Whitlock</div>
    <div class="person-title">Managing Partner</div>
  </div>

  <ul class="contact-list">
    <li>415.555.0143
      <svg viewBox="0 0 20 20" aria-label="Office phone"><path d="M2 7 C2 4 18 4 18 7 L18 9 L14 9 L13 7 L7 7 L6 9 L2 9 Z M5 10 L15 10 L17 17 L3 17 Z"/></svg>
    </li>
    <li>415.555.0167
      <svg viewBox="0 0 20 20" aria-label="Fax"><path d="M5 2 H15 V7 H5 Z M2 8 H18 V15 H15 V12 H5 V15 H2 Z M6 13 H14 V18 H6 Z"/></svg>
    </li>
    <li>415.555.0192
      <svg viewBox="0 0 20 20" aria-label="Mobile"><path d="M5 1 H15 V19 H5 Z M7 3 V15 H13 V3 Z M9 16 H11 V18 H9 Z" fill-rule="evenodd"/></svg>
    </li>
    <li>barn@halcyonridgefund.example
      <svg viewBox="0 0 20 20" aria-label="Email"><path d="M1 4 H19 L10 11 Z M1 6 L10 13 L19 6 V16 H1 Z"/></svg>
    </li>
    <li>817 Fern St San Francisco, CA 94111
      <svg viewBox="0 0 20 20" aria-label="Address"><circle cx="10" cy="10" r="8" fill="none" stroke="#fff" stroke-width="1.6"/><ellipse cx="10" cy="10" rx="3.5" ry="8" fill="none" stroke="#fff" stroke-width="1.4"/><path d="M2 10 H18 M3.5 6 H16.5 M3.5 14 H16.5" stroke="#fff" stroke-width="1.3"/></svg>
    </li>
  </ul>
</section>

</body>
</html>
```